Bref créative
Tern Harbor Inc.
Professional
Dana Pellew
Owner
4817 Birchfield Rd.
Alder Bend, VA 20990
dpellew@ternharborinc.example
www.ternharborinc.example
Would like to use logo from concurrent design effort

```html
<!DOCTYPE html>
<html lang="en">
<head>
<meta charset="utf-8">
<title>Tern Harbor Inc. business cards</title>
<link href="https://fonts.googleapis.com/css2?family=Arimo:ital,wght@0,400;0,700;1,400&display=swap" rel="stylesheet">
<style>
  :root {
    --bg: #ecebe8;
    --card: #ffffff;
    --blue: #2b47a6;
    --red: #e0282e;
    --ink: #4a4a4a;
    --rule: #c9c9c9;
  }
  * { box-sizing: border-box; margin: 0; padding: 0; }
  html, body { width: 1200px; height: 852px; overflow: hidden; }
  body {
    background: var(--bg);
    font-family: "Arimo", Arial, sans-serif;
    color: var(--ink);
    position: relative;
  }
  .card {
    position: absolute;
    width: 540px;
    height: 310px;
    background: var(--card);
    border-radius: 18px;
    overflow: hidden;
    box-shadow: 0 6px 18px rgba(0,0,0,0.18);
  }
  .card--front { left: 70px; top: 110px; }
  .card--back { left: 590px; top: 432px; }
  .swoosh { position: absolute; left: 0; bottom: 0; width: 540px; height: 110px; }
  .brand { position: absolute; display: flex; align-items: center; gap: 12px; }
  .brand__dot {
    width: 34px; height: 34px; border-radius: 50%;
    border: 4px solid var(--blue); flex: none;
  }
  .brand__name { font-weight: 700; font-size: 30px; color: var(--blue); white-space: nowrap; }
  .person__name { font-weight: 700; font-size: 15px; color: var(--blue); }
  .person__role { font-style: italic; font-size: 11px; color: var(--red); margin-top: 3px; }
  .address { font-size: 12px; line-height: 17px; margin-top: 12px; white-space: nowrap; }
  .divider { position: absolute; width: 1px; background: var(--rule); }
  .contacts { list-style: none; font-size: 11.5px; }
  .contacts li { display: flex; align-items: center; gap: 8px; height: 18px; white-space: nowrap; }
  .contacts svg { width: 11px; height: 11px; flex: none; fill: var(--blue); }
  /* front */
  .card--front .brand { left: 110px; top: 44px; }
  .card--front .person { position: absolute; left: 70px; top: 126px; text-align: left; }
  .card--front .divider { left: 218px; top: 124px; height: 112px; }
  .card--front .contacts { position: absolute; left: 234px; top: 122px; }
  /* back */
  .card--back .brand { left: 28px; top: 112px; }
  .card--back .brand__name { font-size: 26px; }
  .card--back .divider { left: 292px; top: 44px; height: 170px; }
  .card--back .person { position: absolute; left: 312px; top: 40px; }
  .card--back .contacts { margin-top: 10px; }
</style>
</head>
<body>

<svg width="0" height="0" style="position:absolute">
  <defs>
    <symbol id="icon-phone" viewBox="0 0 12 12"><path d="M2.5 0.5l2 2-1 1.5c.6 1.4 1.6 2.4 3 3l1.5-1 2 2-1.3 1.6C5.5 9.6 2.4 6.5 1 3z"/></symbol>
    <symbol id="icon-mobile" viewBox="0 0 12 12"><rect x="3" y="0.5" width="6" height="11" rx="1.2"/><rect x="4" y="2" width="4" height="6" fill="#fff"/></symbol>
    <symbol id="icon-mail" viewBox="0 0 12 12"><circle cx="6" cy="6" r="5.5"/><rect x="3" y="4" width="6" height="4" fill="#fff"/><path d="M3 4l3 2.2L9 4" stroke="#2b47a6" stroke-width="0.8" fill="none"/></symbol>
    <symbol id="icon-web" viewBox="0 0 12 12"><circle cx="6" cy="6" r="5.5"/><circle cx="6" cy="6" r="3" fill="#fff"/><circle cx="6" cy="6" r="1.4"/></symbol>
    <symbol id="swoosh" viewBox="0 0 540 110" preserveAspectRatio="none">
      <path d="M0 58 C150 82 330 70 540 8 L540 110 L0 110 Z" fill="#e0282e"/>
      <path d="M0 64 C150 88 330 78 540 18 L540 110 L0 110 Z" fill="#ffffff"/>
      <path d="M0 70 C150 94 330 86 540 26 L540 110 L0 110 Z" fill="#2b47a6"/>
    </symbol>
  </defs>
</svg>

<article class="card card--front">
  <div class="brand">
    <span class="brand__dot"></span>
    <span class="brand__name">Tern Harbor Inc.</span>
  </div>
  <div class="person">
    <p class="person__name">Dana Pellew</p>
    <p class="person__role">Owner</p>
    <p class="address">4817 Birchfield Rd.<br>Alder Bend, VA 20990</p>
  </div>
  <div class="divider"></div>
  <ul class="contacts">
    <li><svg><use href="#icon-mobile"/></svg>555-210-4830</li>
    <li><svg><use href="#icon-phone"/></svg>555-318-2274</li>
    <li><svg><use href="#icon-mail"/></svg>dpellew@ternharborinc.example</li>
    <li><svg><use href="#icon-web"/></svg>www.ternharborinc.example</li>
  </ul>
  <svg class="swoosh"><use href="#swoosh"/></svg>
</article>

<article class="card card--back">
  <div class="brand">
    <span class="brand__dot"></span>
    <span class="brand__name">Tern Harbor Inc.</span>
  </div>
  <div class="divider"></div>
  <div class="person">
    <p class="person__name">Dana Pellew</p>
    <p class="person__role">Owner</p>
    <p class="address">4817 Birchfield Rd.<br>Alder Bend, VA 20990</p>
    <ul class="contacts">
      <li><svg><use href="#icon-phone"/></svg>555-210-4830</li>
      <li><svg><use href="#icon-mobile"/></svg>555-318-2274</li>
      <li><svg><use href="#icon-mail"/></svg>dpellew@ternharborinc.example</li>
      <li><svg><use href="#icon-web"/></svg>www.ternharborinc.example</li>
    </ul>
  </div>
  <svg class="swoosh"><use href="#swoosh"/></svg>
</article>

</body>
</html>
```